Electrical contractor in San Diego county since 1988

Provide a company name/ logo for business cards and forms. Newer and more modern old card is attached. Color preference is black and orange. Simple and streamlined nothing too busy. I have also attached a card that represents the simplicity of what we are looking for.

Contractor

```html
<!DOCTYPE html>
<html lang="en">
<head>
<meta charset="utf-8">
<title>K.M. Electric Inc. – Business Card</title>
<link rel="stylesheet" href="https://fonts.googleapis.com/css2?family=Lato:wght@400;700;900&display=swap">
<style>
  :root {
    --backdrop: #262626;
    --card-dark: #2b2828;
    --card-light: #ffffff;
    --accent: #f4c21a;
    --ink-strong: #3a3a3a;
    --ink-soft: #555555;
    --ink-inverse: #ffffff;
  }
  * { box-sizing: border-box; margin: 0; padding: 0; }
  html, body {
    width: 1200px;
    height: 900px;
    overflow: hidden;
    background: var(--backdrop);
    font-family: "Lato", sans-serif;
  }
  .canvas {
    position: relative;
    width: 1200px;
    height: 900px;
    display: flex;
    align-items: center;
    justify-content: center;
  }
  .card {
    position: relative;
    width: 1050px;
    height: 600px;
    box-shadow: 0 20px 50px rgba(0,0,0,0.5);
    overflow: hidden;
  }
  .card__shape {
    position: absolute;
    inset: 0;
    width: 100%;
    height: 100%;
  }
  .brand {
    position: absolute;
    left: 70px;
    top: 225px;
  }
  .brand__name {
    font-weight: 900;
    font-size: 46px;
    color: var(--accent);
    line-height: 1;
    margin-bottom: 12px;
  }
  .brand__service {
    font-weight: 700;
    font-size: 21px;
    color: var(--ink-strong);
    line-height: 1.25;
  }
  .brand__license {
    font-weight: 400;
    font-size: 21px;
    color: var(--ink-soft);
    line-height: 1.25;
  }
  .contact {
    position: absolute;
    left: 690px;
    top: 210px;
    color: var(--ink-inverse);
  }
  .contact__name {
    font-weight: 900;
    font-size: 29px;
    text-transform: uppercase;
    line-height: 1;
  }
  .contact__role {
    font-size: 19px;
    color: var(--accent);
    margin-top: 4px;
    margin-left: 4px;
  }
  .contact__group {
    display: flex;
    gap: 12px;
    margin-top: 34px;
    font-size: 21px;
    line-height: 1.2;
  }
  .contact__icons {
    display: flex;
    flex-direction: column;
    gap: 4px;
    padding-top: 2px;
  }
  .contact__icon { width: 22px; height: 21px; fill: var(--accent); }
  .contact__group--address { margin-top: 26px; }
</style>
</head>
<body>
<main class="canvas">
  <article class="card">
    <svg class="card__shape" viewBox="0 0 1050 600" preserveAspectRatio="none" aria-hidden="true">
      <rect width="1050" height="600" fill="var(--card-dark)"/>
      <path d="M0 0 H610 C700 150 660 420 440 600 H0 Z" fill="var(--card-light)"/>
      <path d="M610 0 H618 C712 150 680 430 468 600 H440 C660 420 700 150 610 0 Z" fill="var(--accent)"/>
    </svg>

    <section class="brand">
      <h1 class="brand__name">K.M. Electric Inc.</h1>
      <p class="brand__service">Commercial - New &amp; Remodel</p>
      <p class="brand__license">Lic. 704215</p>
    </section>

    <section class="contact">
      <h2 class="contact__name">Daniel Hale</h2>
      <p class="contact__role">President</p>

      <div class="contact__group">
        <div class="contact__icons">
          <svg class="contact__icon" viewBox="0 0 24 24" aria-label="Phone"><path d="M2 7c0-2 4-4 10-4s10 2 10 4v2h-5V7c-2-.8-8-.8-10 0v2H2z"/><path d="M6 11h12l3 9H3z"/><circle cx="12" cy="15" r="2.5" fill="var(--card-dark)"/></svg>
          <svg class="contact__icon" viewBox="0 0 24 24" aria-label="Fax"><path d="M6 2h12v6H6z"/><path d="M2 9h20v9h-4v-4H6v4H2z"/><path d="M7 15h10v7H7z"/></svg>
        </div>
        <div>
          <p>(619) 555-0142</p>
          <p>(619) 555-0187</p>
        </div>
      </div>

      <div class="contact__group contact__group--address">
        <svg class="contact__icon" viewBox="0 0 24 24" aria-label="Address"><path d="M12 1a8 8 0 0 0-8 8c0 6 8 14 8 14s8-8 8-14a8 8 0 0 0-8-8zm0 11a3 3 0 1 1 0-6 3 3 0 0 1 0 6z"/></svg>
        <div>
          <p>P.O. Box 2471</p>
          <p>Cedar Ridge, CA 92000-0123</p>
        </div>
      </div>
    </section>
  </article>
</main>
</body>
</html>
```